Business Card for Willowcrest Terrain Advisors

We need a business card for Willowcrest Terrain Advisors. The company website address is provided below. The company logo is attached. We provide specialized permafrost services to the mining, transportation, and oil & gas industries. The card should be prepared for:
Dominic Halloway, PhD.
Willowcrest Terrain Advisors
PO Box 418529
Birch Hollow, Alaska 99612
Direct: +1-907-555-2964
Email: dhalloway@terrainadvisors-example.com
Website: www.willowcrestterrainadvisors-example.com

```html
<!DOCTYPE html>
<html lang="en">
<head>
<meta charset="utf-8">
<title>Willowcrest Terrain Advisors – Business Card</title>
<link href="https://fonts.googleapis.com/css2?family=Quicksand:wght@400;500;600;700&display=swap" rel="stylesheet">
<style>
  :root {
    --backdrop: #ababab;
    --card-front: #ffffff;
    --card-back: #2b2b2b;
    --card-back-edge: #1f1f1f;
    --ink: #1f2328;
    --ink-soft: #3d3d3d;
    --rule: #8a8a8a;
    --shadow: rgba(0, 0, 0, 0.28);
  }
  * { box-sizing: border-box; margin: 0; padding: 0; }
  html, body {
    width: 1200px; height: 1000px; overflow: hidden;
    background: var(--backdrop);
    font-family: "Quicksand", sans-serif;
    color: var(--ink-soft);
  }
  .stage { position: relative; width: 1200px; height: 1000px; }
  .card {
    position: absolute; left: 293px; width: 615px; height: 354px;
    border-radius: 14px;
    box-shadow: 0 3px 8px var(--shadow);
    overflow: hidden;
  }
  .card--back {
    top: 132px;
    background: linear-gradient(120deg, var(--card-back-edge), var(--card-back) 60%, #333333);
  }
  .card--front { top: 530px; background: var(--card-front); }

  .brand-name {
    position: absolute; left: 0; right: 0; top: 46px;
    text-align: center;
    font-weight: 700; font-size: 19px; letter-spacing: 1.5px;
    color: var(--ink);
  }
  .holder {
    position: absolute; right: 321px; top: 184px;
    text-align: right;
  }
  .holder__name { font-weight: 700; font-size: 13.5px; letter-spacing: 0.3px; line-height: 18px; }
  .holder__company { font-weight: 400; font-size: 13.5px; line-height: 18px; }
  .divider {
    position: absolute; left: 307px; top: 158px; width: 1px; height: 87px;
    background: var(--rule);
  }
  .contact {
    position: absolute; left: 319px; top: 159px;
    font-size: 13.5px; line-height: 17px; font-weight: 400;
  }
  .contact__address { margin-bottom: 13px; }
  .contact__line { display: flex; align-items: center; gap: 7px; white-space: nowrap; }
  .contact__line svg { width: 12px; height: 11px; fill: var(--ink-soft); flex: none; }
  .contact__email { font-size: 12.8px; }
  .website {
    position: absolute; left: 0; right: 0; top: 311px;
    text-align: center; font-size: 13.5px; color: var(--ink-soft);
  }
  .website__domain { font-weight: 500; }
  .website__tld { font-weight: 400; }
</style>
</head>
<body>
<main class="stage">
  <section class="card card--back" role="img" aria-label="Card back: faint repeating company name pattern on dark charcoal"></section>

  <section class="card card--front">
    <div class="brand-name">WILLOWCREST TERRAIN ADVISORS</div>

    <div class="holder">
      <p class="holder__name">DOMINIC HALLOWAY, PHD.</p>
      <p class="holder__company">Willowcrest Terrain Advisors</p>
    </div>

    <div class="divider"></div>

    <div class="contact">
      <p class="contact__address">PO Box 418529<br>Birch Hollow, Alaska 99612</p>
      <p class="contact__line">
        <svg viewBox="0 0 12 12" aria-hidden="true"><path d="M2.6 0.6l2 2.2-1 1.4c.7 1.5 1.8 2.6 3.3 3.3l1.4-1 2.2 2-1.2 2.3C5 10.5 1.5 7 .4 1.8z"/></svg>
        (907) 555-2964
      </p>
      <p class="contact__line contact__email">
        <svg viewBox="0 0 12 9" aria-hidden="true"><path d="M0 0h12L6 4.6z"/><path d="M0 1.4l6 4.6 6-4.6V9H0z"/></svg>
        dhalloway@terrainadvisors-example.com
      </p>
    </div>

    <p class="website"><span class="website__domain">willowcrestterrainadvisors-example</span><span class="website__tld">.com</span></p>
  </section>
</main>
</body>
</html>
```